Simple landing page for Brindleys cookbook

I need a one page landingpage where customers can order the cookbook.
This is a cookbook of a collection of recipes from our deli that we used to run.
I need a landing page where customers can come and order the book. I also need it coded. I already have the domain through hostmoxa.
I can send the file of the book through wetransfer. It's too big to upload here. Just so you get the feel that I am looking for.
I attached a simple text as an introduction to the page. But I am open to any suggestions. I want it all to be about the experience that we are sharing the recipes with everybody and that it's for sale. The book is $29.99, shipping included.
Customers have to be able to click and buy the book from it.

Coding

Coded - Design and coding required

Number of Pages Required

1 page

Font styles to use
Sans Serif

Requirements
Must have
• Same colors as the cookbook

```html
<!DOCTYPE html>
<html lang="en">
<head>
<meta charset="utf-8">
<title>Brindleys Sandwiches – The Cookbook</title>
<link rel="stylesheet" href="https://fonts.googleapis.com/css2?family=Domine:wght@700&family=Heebo:wght@400;500;700&display=swap">
<style>
:root{
  --green:#678a29;
  --pink:#c8184a;
  --page:#f1f9fd;
  --hero:#c6e2ee;
  --ink:#1b1b1b;
  --white:#ffffff;
}
*{margin:0;padding:0;box-sizing:border-box}
html,body{width:1200px;height:2501px;overflow:hidden}
body{position:relative;background:var(--page);font-family:"Heebo",sans-serif;color:var(--ink)}
.abs{position:absolute}
.heading{font-family:"Domine",serif;font-weight:700;line-height:1.2;color:var(--ink)}

.site-header{left:0;top:0;width:1200px;height:70px;background:var(--green)}
.brand{left:101px;top:12px;font-weight:700;font-size:36px;color:var(--white);letter-spacing:.5px}
.nav-preview{left:795px;top:24px;font-weight:700;font-size:16px;color:var(--white);text-decoration:none}
.nav-buy{left:944px;top:0;width:157px;height:70px;background:var(--pink);color:var(--white);font-weight:700;font-size:16px;display:flex;align-items:center;justify-content:center;gap:8px;text-decoration:none}

.hero{left:0;top:70px;width:1200px;height:682px;background:radial-gradient(circle at 80% 30%,#d6ebf3 0%,var(--hero) 55%,#b9dae8 100%)}
.hero-title{left:101px;top:208px;width:530px;font-size:42px;line-height:53px}
.hero-text{left:101px;top:385px;width:520px;font-size:17.5px;line-height:32px;letter-spacing:-.1px}
.btn{display:flex;align-items:center;justify-content:center;width:200px;height:54px;border-radius:27px;font-weight:500;font-size:17px;text-decoration:none;text-transform:uppercase}
.btn-solid{background:var(--green);color:var(--white)}
.btn-outline{border:2px solid var(--green);color:var(--green)}
.btn-light{border:2px solid var(--white);color:var(--white)}
.hero-note{left:102px;top:584px;font-size:16.5px}
.book-cover{left:665px;top:138px;width:350px;height:512px;border-radius:3px;background:linear-gradient(160deg,#e9f4fa 0%,#cfe3ee 30%,#b88a4e 55%,#d9c3a8 75%,#f1f4f6 100%);box-shadow:18px 14px 30px rgba(40,70,90,.25)}

.photo{top:764px;height:204px}
.ph1{left:0;width:84px;background:linear-gradient(#8c5a2e,#4f7a2a)}
.ph2{left:97px;width:231px;background:linear-gradient(135deg,#c99356,#5c8a3a 60%,#b7472e)}
.ph3{left:341px;width:232px;background:linear-gradient(135deg,#7a4a26,#d9a15a 50%,#e9e4dc)}
.ph4{left:586px;width:232px;background:linear-gradient(160deg,#2f3a44,#c7983f 50%,#e6e1da)}
.ph5{left:831px;width:231px;background:linear-gradient(160deg,#2e2119,#c7832f 45%,#5a3a24)}
.ph6{left:1075px;width:125px;background:linear-gradient(135deg,#d4a66a,#a8b58c 60%,#eae3d7)}

.welcome-title{left:0;top:1042px;width:1200px;text-align:center;font-size:42px}
.welcome-text{left:130px;top:1116px;width:940px;text-align:center;font-size:15px;line-height:29.5px;letter-spacing:-.15px}
.welcome-text p+p{margin-top:20px}

.author-photo{left:0;top:1429px;width:601px;height:513px;background:linear-gradient(180deg,#e8ebee 0%,#dfe3e6 55%,#a9c9a4 75%,#6e6a62 100%)}
.author-panel{left:601px;top:1429px;width:599px;height:513px;background:var(--green)}
.author-title{left:635px;top:1502px;font-size:42px;color:var(--white)}
.author-text{left:635px;top:1573px;width:475px;font-size:15px;line-height:29px;letter-spacing:-.15px;color:var(--white)}
.author-text p+p{margin-top:10px}

.pages-title{left:101px;top:2027px;font-size:42px;line-height:50px}
.pages-text{left:101px;top:2145px;width:440px;font-size:15px;line-height:29px;letter-spacing:-.1px}
.open-book{left:590px;top:2045px;width:515px;height:285px;background:linear-gradient(120deg,#8f9a86 0%,#c9cfc0 45%,#f4f5f2 100%)}

.site-footer{left:0;top:2437px;width:1200px;height:64px;background:var(--green);color:var(--white);display:flex;align-items:center;justify-content:center;font-size:15.5px}
</style>
</head>
<body>
<header class="abs site-header">
  <div class="abs brand">BRINDLEYS</div>
  <a class="abs nav-preview" href="#preview">GET A PREVIEW</a>
  <a class="abs nav-buy" href="#buy">
    <svg width="16" height="14" viewBox="0 0 16 14" aria-hidden="true"><path d="M0 1h3l2 8h8l2-6H4.5" fill="none" stroke="#fff" stroke-width="2"/><circle cx="6" cy="12" r="1.5" fill="#fff"/><circle cx="12" cy="12" r="1.5" fill="#fff"/></svg>
    BUY NOW
  </a>
</header>

<section class="abs hero"></section>
<h1 class="abs heading hero-title">Your Ultimate Guide To Creating Your Own Favourite</h1>
<p class="abs hero-text">Lorem ipsum dolor sit amet, consectetur adipiscing elit, sed do eiusmod tempor incididunt ut labore et dolore magna aliqua. Quis ipsum suspendisse ultrices gravida.</p>
<a class="abs btn btn-solid" id="buy" href="#buy" style="left:102px;top:511px">Buy for $29.99</a>
<a class="abs btn btn-outline" id="preview" href="#preview" style="left:327px;top:511px">Get a preview</a>
<p class="abs hero-note">Price does not include taxes. Shipping &amp; handling rates apply.</p>
<div class="abs book-cover" role="img" aria-label="Cookbook cover with a stacked sandwich on a plate"></div>

<div class="abs photo ph1" role="img" aria-label="Sandwich with sprouts and tomato"></div>
<div class="abs photo ph2" role="img" aria-label="Grilled chicken panini halves"></div>
<div class="abs photo ph3" role="img" aria-label="Fried patty bun on a plate with chilli"></div>
<div class="abs photo ph4" role="img" aria-label="Toasted egg sandwich on a board"></div>
<div class="abs photo ph5" role="img" aria-label="Burger with fries on paper"></div>
<div class="abs photo ph6" role="img" aria-label="Chicken burger in a paper box"></div>

<h2 class="abs heading welcome-title">Welcome to Brindleys</h2>
<div class="abs welcome-text">
  <p>Opening it’s doors in January of 2010, Brindleys European Deli was a sandwich shop in Alderbrook, Eastvale, but also a lot more than that. We spent five years with this business until it’s eventual closure in April of 2015. It was a special time where we met tons of amazing people, who we loved to see and serve. Brindleys started out as a deli but eventually morphed into the sandwich shop we all know it as today.</p>
  <p>We are overwhelmed with the continuous positive messages and comments we get on our Friendbook page that is still up and running. Unfortunately, we can’t open another Brindleys, but we can offer you this collection of our recipes for you to try out at home with your family and friends. We truly hope you will enjoy making these sandwiches just as much as we did. If you do, please post your pictures of you making a meal or the finished product, or even enjoying it!</p>
</div>

<div class="abs author-photo" role="img" aria-label="Author in a kitchen holding the cookbook"></div>
<section class="abs author-panel"></section>
<h2 class="abs heading author-title">About Mara Quill</h2>
<div class="abs author-text">
  <p>Lorem ipsum dolor sit amet, consectetur adipiscing elit, sed do eiusmod tempor incididunt ut labore et do magna aliqua. Quis ipsum suspendisse ultrices gravida. Risus commodo viverra maecenas accumsan lacus vel facilisis.</p>
  <p>Lorem ipsum dolor sit amet, consectetur adipiscing elit, sed do eiusmod tempor incididunt ut labore et do magna aliqua. Quis ipsum suspendisse ultrices gravida.</p>
</div>
<a class="abs btn btn-light" href="#bio" style="left:635px;top:1803px;width:200px;height:53px">Full biography</a>

<h2 class="abs heading pages-title">From The Pages<br>To The Table</h2>
<p class="abs pages-text">Lorem ipsum dolor sit amet, consectetur ang elit, sed do eiusmod tempor incididunt ut labore et do mliqua. Quis ipsum suspendisse ultrices gravida. Risus commodo viverra maecenas accumsan lacus vel facilisis.</p>
<a class="abs btn btn-solid" href="#buy" style="left:102px;top:2294px">Buy for $29.99</a>
<a class="abs btn btn-outline" href="#sample" style="left:327px;top:2294px">Try a sample</a>
<div class="abs open-book" role="img" aria-label="Open cookbook showing a sandwich photo and recipe page"></div>

<footer class="abs site-footer">© Copyright | Brindleys 2021. All Right Reserved</footer>
</body>
</html>
```